Velmar Ops Business Cards

We need to design some upbeat business cards. We are an Industrial Rope Access Company/Height Safety Company that specialize in Rope Access, Confined Space, Anchor Points, Safety Systems, PPE Inspecions and Rigging.
Company name is Velmar Ops Ltd
Card is for Gareth Lomas the Company Director
His mobile number is 027 418 9072 and email is gareth@velmarops.co.nz. Website address is www.velmarops.co.nz.
We will post some pictures below to ensure you get a good idea of what we do.

```html
<!DOCTYPE html>
<html lang="en">
<head>
<meta charset="utf-8">
<title>Velmar Ops Business Cards</title>
<link rel="stylesheet" href="https://fonts.googleapis.com/css2?family=Exo+2:wght@400;600;700;800&family=Mulish:wght@400;500&display=swap">
<style>
  :root {
    --page-bg: #b9b9b9;
    --navy-top: #0e2d63;
    --navy-bottom: #044a8c;
    --brand-blue: #0a5a9c;
    --card-white: #f1f1f1;
    --ink: #2b2b2b;
    --light-text: #e9edf3;
    --dot: #4f7fb5;
    --photo-frame: #dfe5ee;
  }
  * { box-sizing: border-box; margin: 0; padding: 0; }
  html, body { width: 1200px; height: 576px; overflow: hidden; }
  body {
    background: var(--page-bg);
    position: relative;
    font-family: "Mulish", sans-serif;
  }
  .card {
    position: absolute;
    border-radius: 13px;
    overflow: hidden;
  }
  .card-front {
    left: 82px; top: 138px; width: 484px; height: 294px;
    background: linear-gradient(180deg, var(--navy-top) 0%, #083c7a 55%, var(--navy-bottom) 100%);
  }
  .card-back {
    left: 602px; top: 138px; width: 480px; height: 291px;
    background: var(--card-white);
  }
  .front-wordmark {
    position: absolute; left: 0; right: 0; top: 48px;
    text-align: center;
    font-family: "Exo 2", sans-serif;
    font-weight: 800;
    font-size: 46px;
    color: var(--light-text);
    letter-spacing: 0.5px;
  }
  .photo-strip {
    position: absolute; left: 22px; top: 138px;
    display: flex; gap: 5px;
  }
  .photo {
    width: 106px; height: 80px;
    border: 2px solid var(--photo-frame);
  }
  .photo-tank { background: linear-gradient(135deg, #3d3a33, #8a8677 50%, #2e2c27); }
  .photo-rig { background: linear-gradient(180deg, #4f7fc2, #8db0dd 60%, #5a6470); }
  .photo-tower { background: linear-gradient(160deg, #b9c8da, #7f8a98 55%, #c48c8f); }
  .photo-facade { background: linear-gradient(90deg, #2b2b2d 60%, #b8c2cc); }
  .services {
    position: absolute; left: 0; right: 0; top: 236px;
    text-align: center;
    font-family: "Exo 2", sans-serif;
    font-weight: 600;
    font-size: 16px;
    line-height: 21px;
    color: var(--light-text);
  }
  .services .sep { color: var(--dot); margin: 0 7px; }
  .holder-name {
    position: absolute; left: 23px; top: 44px;
    font-family: "Exo 2", sans-serif;
    font-weight: 700; font-size: 22px;
    color: var(--brand-blue);
  }
  .holder-role {
    position: absolute; left: 23px; top: 73px;
    font-size: 12px; color: var(--ink);
  }
  .back-wordmark {
    position: absolute; right: 34px; top: 44px;
    font-family: "Exo 2", sans-serif;
    font-weight: 800; font-size: 36px;
    color: var(--brand-blue);
  }
  .contact-list {
    position: absolute; left: 23px; top: 210px;
    list-style: none;
    font-size: 12.5px; color: var(--ink);
  }
  .contact-list li { display: flex; align-items: center; height: 17.5px; }
  .contact-list svg { width: 10px; height: 10px; margin-right: 13px; fill: var(--brand-blue); }
  .contact-list .accent { color: var(--brand-blue); }
</style>
</head>
<body>
  <section class="card card-front" aria-label="Card front">
    <div class="front-wordmark">Velmar Ops</div>
    <div class="photo-strip">
      <div class="photo photo-tank" role="img" aria-label="Photo of a technician working inside a steel tank"></div>
      <div class="photo photo-rig" role="img" aria-label="Photo of rigging on a crane structure against blue sky"></div>
      <div class="photo photo-tower" role="img" aria-label="Photo of rope access workers on a tall building"></div>
      <div class="photo photo-facade" role="img" aria-label="Photo of a worker on a dark building facade"></div>
    </div>
    <p class="services">
      Rope Access<span class="sep">•</span>Anchor Points<span class="sep">•</span>PPE Certification<br>
      Confined Space<span class="sep">•</span>Safety Systems<span class="sep">•</span>Rigging
    </p>
  </section>

  <section class="card card-back" aria-label="Card back">
    <h1 class="holder-name">Gareth Lomas</h1>
    <p class="holder-role">Director</p>
    <div class="back-wordmark">Velmar Ops</div>
    <ul class="contact-list">
      <li>
        <svg viewBox="0 0 10 10" aria-hidden="true"><path d="M1 3.2C1 2 2 1.5 5 1.5S9 2 9 3.2V4H7V3H3v1H1z M2.5 5h5L9 8.5H1z"/></svg>
        027 418 9072
      </li>
      <li>
        <svg viewBox="0 0 10 10" aria-hidden="true"><path d="M0.5 2h9v6h-9z M1.2 2.6L5 5.6l3.8-3" fill="none" stroke="#0a5a9c" stroke-width="1"/></svg>
        gareth@velmarops.co.nz
      </li>
      <li>
        <svg viewBox="0 0 10 10" aria-hidden="true"><circle cx="5" cy="5" r="4.2" fill="none" stroke="#0a5a9c" stroke-width="1"/><path d="M0.8 5h8.4M5 0.8v8.4M5 0.8C3 3 3 7 5 9.2M5 0.8C7 3 7 7 5 9.2" fill="none" stroke="#0a5a9c" stroke-width="0.8"/></svg>
        www.<span class="accent">velmarops</span>.co.nz
      </li>
    </ul>
  </section>
</body>
</html>
```